Assorted Banner Ads

Create standard sized banner ads (300x250, 728x90, 160x600) using logo and create exciting ads using collateral provided and your own ideas.

```html
<!DOCTYPE html>
<html lang="en">
<head>
<meta charset="utf-8">
<title>Harbor Lane Room Escape – Banner Set</title>
<link rel="stylesheet" href="https://fonts.googleapis.com/css2?family=Michroma&family=Montserrat:wght@600;700;800&family=Saira+Semi+Expanded:wght@600;700&display=swap">
<style>
  :root{
    --parchment:#e6dcbf;
    --forest:#0f4f22;
    --forest-deep:#0a3a18;
    --leaf:#1f8a3a;
    --leaf-bright:#2fa84b;
    --mist:#b9d6bf;
    --ink:#1d2219;
    --white:#ffffff;
    --stage:#efece6;
    --font-brand:"Michroma", sans-serif;
    --font-head:"Montserrat", sans-serif;
    --font-list:"Saira Semi Expanded", sans-serif;
  }
  *{box-sizing:border-box;margin:0;padding:0}
  html,body{width:1200px;height:1200px;overflow:hidden;background:var(--stage)}
  .canvas{position:relative;width:1200px;height:1200px}
  .banner{position:absolute;overflow:hidden;background:var(--parchment);box-shadow:0 3px 10px rgba(0,0,0,.18)}
  .banner svg.backdrop{position:absolute;inset:0;width:100%;height:100%}
  .abs{position:absolute}

  .brand{text-align:center;color:var(--ink);font-family:var(--font-brand);line-height:1.15}
  .brand .mark{display:block;margin:0 auto;background:var(--leaf)}
  .brand .name{display:block;letter-spacing:.06em}
  .brand .sub{display:block;letter-spacing:.28em}

  .headline{color:var(--white);font-family:var(--font-head);text-shadow:0 2px 3px rgba(0,0,0,.55);white-space:nowrap}
  .headline .lead{display:block;font-weight:700;font-variant:small-caps;letter-spacing:.08em;line-height:1}
  .headline .big{display:block;font-weight:800;line-height:1}

  .rooms{list-style:none;color:var(--white);font-family:var(--font-list);font-weight:700;text-shadow:0 1px 2px rgba(0,0,0,.6)}
  .rooms li{position:relative;white-space:nowrap}
  .rooms li::before{content:"";position:absolute;left:0;top:50%;background:var(--leaf-bright);transform:translateY(-50%)}

  .cta{display:flex;align-items:center;justify-content:center;color:var(--ink);font-family:var(--font-head);font-weight:600;letter-spacing:.02em;white-space:nowrap;
       background:linear-gradient(180deg,#7bc98e 0%,#2e9a4a 45%,#1f7d37 100%);border:2px solid #4cb865;border-radius:8px;box-shadow:0 2px 4px rgba(0,0,0,.3)}
  .url{color:var(--leaf);font-family:var(--font-head);font-weight:700;text-align:center;white-space:nowrap}

  /* leaderboard 728x90 */
  .leaderboard{left:43px;top:94px;width:1113px;height:137px}
  .leaderboard .brand{left:0;top:22px;width:170px}
  .leaderboard .mark{width:24px;height:24px;margin-bottom:16px}
  .leaderboard .name{font-size:15px}
  .leaderboard .sub{font-size:8px;margin-top:3px}
  .leaderboard .headline{left:230px;top:28px}
  .leaderboard .lead{font-size:34px}
  .leaderboard .big{font-size:38px;margin-top:8px}
  .leaderboard .rooms{left:608px;top:24px;font-size:14px;line-height:22.5px}
  .leaderboard .rooms li{padding-left:18px}
  .leaderboard .rooms li::before{width:9px;height:9px}
  .leaderboard .cta{left:897px;top:46px;width:188px;height:35px;font-size:18px}
  .leaderboard .url{left:880px;top:91px;width:222px;font-size:10px}

  /* skyscraper 160x600 */
  .skyscraper{left:43px;top:274px;width:224px;height:838px}
  .skyscraper .brand{left:0;top:24px;width:224px}
  .skyscraper .mark{width:24px;height:24px;margin-bottom:18px}
  .skyscraper .name{font-size:19px}
  .skyscraper .sub{font-size:10px;margin-top:5px}
  .skyscraper .headline{left:0;top:276px;width:224px;text-align:center}
  .skyscraper .lead{font-size:32px;line-height:34px}
  .skyscraper .big{font-size:38px;line-height:43px;margin-top:12px}
  .skyscraper .rooms{left:14px;top:473px;font-size:12.5px;line-height:18.5px}
  .skyscraper .rooms li{padding-left:15px}
  .skyscraper .rooms li::before{width:8px;height:8px}
  .skyscraper .cta{left:23px;top:744px;width:173px;height:32px;font-size:17px}
  .skyscraper .url{left:0;top:787px;width:224px;font-size:9.5px}

  /* medium rectangle 300x250 */
  .rectangle{left:342px;top:279px;width:664px;height:554px}
  .rectangle .brand{left:0;top:22px;width:664px}
  .rectangle .mark{width:26px;height:26px;margin-bottom:22px}
  .rectangle .name{font-size:23px}
  .rectangle .sub{font-size:12px;margin-top:6px}
  .rectangle .headline{left:0;top:228px;width:664px;text-align:center}
  .rectangle .lead{font-size:50px}
  .rectangle .big{font-size:56px;margin-top:10px}
  .rectangle .rooms{top:362px;font-size:18px;line-height:24px}
  .rectangle .rooms.col-a{left:78px}
  .rectangle .rooms.col-b{left:366px}
  .rectangle .rooms li{padding-left:22px}
  .rectangle .rooms li::before{width:12px;height:12px}
  .rectangle .cta{left:191px;top:444px;width:273px;height:50px;font-size:27px;border-radius:10px}
  .rectangle .url{left:0;top:504px;width:664px;font-size:25px}
</style>
</head>
<body>
<main class="canvas">

  <!-- Leaderboard -->
  <section class="banner leaderboard" aria-label="Leaderboard banner">
    <svg class="backdrop" viewBox="0 0 1113 137" preserveAspectRatio="none" aria-hidden="true">
      <defs>
        <linearGradient id="lb-scene" x1="0" y1="0" x2="1" y2="0">
          <stop offset="0" stop-color="#0f4f22"/><stop offset=".5" stop-color="#3d7a2a"/><stop offset="1" stop-color="#0f4f22"/>
        </linearGradient>
      </defs>
      <rect width="1113" height="137" fill="var(--parchment)"/>
      <path d="M180 0 Q140 68 180 137 L875 137 Q835 68 875 0 Z" fill="var(--leaf)"/>
      <path d="M190 0 Q152 68 190 137 L870 137 Q828 68 870 0 Z" fill="var(--mist)"/>
      <path d="M198 0 Q162 68 198 137 L862 137 Q820 68 862 0 Z" fill="var(--forest)"/>
    </svg>
    <svg class="abs" role="img" aria-label="Green-tinted photo of an antique study with brass lamps and glassware" viewBox="0 0 1113 137" preserveAspectRatio="none" style="left:0;top:0;width:1113px;height:137px">
      <path d="M198 0 Q162 68 198 137 L862 137 Q820 68 862 0 Z" fill="url(#lb-scene)" opacity=".7"/>
    </svg>
    <div class="abs brand">
      <span class="mark"></span>
      <span class="name">HARBOR LANE</span>
      <span class="sub">ROOM ESCAPE</span>
    </div>
    <h2 class="abs headline"><span class="lead">Can You Escape</span><span class="big">IN 60 MINUTES?</span></h2>
    <ul class="abs rooms">
      <li>Escape The Vault</li><li>Captain's Gold Quest</li><li>Island Jail Break</li><li>Cutter Escape</li>
    </ul>
    <a class="abs cta">ESCAPE NOW</a>
    <p class="abs url">www.harborlaneescape.com</p>
  </section>

  <!-- Skyscraper -->
  <section class="banner skyscraper" aria-label="Skyscraper banner">
    <svg class="backdrop" viewBox="0 0 224 838" preserveAspectRatio="none" aria-hidden="true">
      <defs>
        <radialGradient id="sk-scene" cx=".45" cy=".45" r=".6">
          <stop offset="0" stop-color="#5f8f2e"/><stop offset="1" stop-color="#0f4f22"/>
        </radialGradient>
      </defs>
      <rect width="224" height="838" fill="var(--parchment)"/>
      <path d="M0 148 Q112 200 224 148 L224 690 Q112 620 0 690 Z" fill="var(--leaf-bright)"/>
      <path d="M0 165 Q112 214 224 165 L224 676 Q112 606 0 676 Z" fill="var(--forest)"/>
    </svg>
    <svg class="abs" role="img" aria-label="Green-tinted photo of an antique study with a lamp and old books" viewBox="0 0 224 838" preserveAspectRatio="none" style="left:0;top:0;width:224px;height:838px">
      <path d="M0 165 Q112 214 224 165 L224 676 Q112 606 0 676 Z" fill="url(#sk-scene)" opacity=".85"/>
    </svg>
    <div class="abs brand">
      <span class="mark"></span>
      <span class="name">HARBOR LANE</span>
      <span class="sub">ROOM ESCAPE</span>
    </div>
    <h2 class="abs headline"><span class="lead">Can You<br>Escape</span><span class="big">IN 60<br>MINUTES?</span></h2>
    <ul class="abs rooms">
      <li>Escape The Vault</li><li>Captain's Gold Quest</li><li>Island Jail Break</li><li>Cutter Escape</li>
    </ul>
    <a class="abs cta">ESCAPE NOW</a>
    <p class="abs url">www.harborlaneescape.com</p>
  </section>

  <!-- Medium rectangle -->
  <section class="banner rectangle" aria-label="Medium rectangle banner">
    <svg class="backdrop" viewBox="0 0 664 554" preserveAspectRatio="none" aria-hidden="true">
      <defs>
        <linearGradient id="mr-scene" x1="0" y1="0" x2="1" y2="0">
          <stop offset="0" stop-color="#2f6a25"/><stop offset=".45" stop-color="#4f8a32"/><stop offset=".82" stop-color="#5f9e80"/><stop offset="1" stop-color="#0f4f22"/>
        </linearGradient>
      </defs>
      <rect width="664" height="554" fill="var(--parchment)"/>
      <path d="M0 92 Q332 258 664 92 L664 478 Q332 430 0 478 Z" fill="var(--leaf-bright)"/>
      <path d="M0 104 Q332 268 664 104 L664 466 Q332 420 0 466 Z" fill="var(--mist)"/>
      <path d="M0 112 Q332 278 664 112 L664 460 Q332 414 0 460 Z" fill="var(--forest)"/>
    </svg>
    <svg class="abs" role="img" aria-label="Green-tinted photo of an antique study with glassware, a lamp and a window" viewBox="0 0 664 554" preserveAspectRatio="none" style="left:0;top:0;width:664px;height:554px">
      <path d="M0 112 Q332 278 664 112 L664 400 Q332 380 0 400 Z" fill="url(#mr-scene)" opacity=".6"/>
    </svg>
    <div class="abs brand">
      <span class="mark"></span>
      <span class="name">HARBOR LANE</span>
      <span class="sub">ROOM ESCAPE</span>
    </div>
    <h2 class="abs headline"><span class="lead">Can You Escape</span><span class="big">IN 60 MINUTES?</span></h2>
    <ul class="abs rooms col-a"><li>Escape The Vault</li><li>Captain's Gold Quest</li></ul>
    <ul class="abs rooms col-b"><li>Island Jail Break</li><li>Cutter Escape</li></ul>
    <a class="abs cta">ESCAPE NOW</a>
    <p class="abs url">www.harborlaneescape.com</p>
  </section>

</main>
</body>
</html>
```